Business Card Design for The Brightwell Apparel House

Outlet Designer Clothing & Accessories Retailer

The Brightwell Apparel House is a high-end luxury outlet retailer. There is a wide selection of brands sold in the store that are from the most famous designer houses in Italy, France & Germany such

```html
<!DOCTYPE html>
<html lang="en">
<head>
<meta charset="utf-8">
<title>Brightwell Apparel House – Business Card</title>
<link href="https://fonts.googleapis.com/css2?family=Jost:wght@400;500;600&display=swap" rel="stylesheet">
<style>
  :root {
    --ink: #0b0b0b;
    --paper: #ffffff;
    --stage: #f1f1f1;
    --muted: #444444;
  }
  * { box-sizing: border-box; margin: 0; padding: 0; }
  html, body { width: 1200px; height: 631px; overflow: hidden; }
  body {
    background: var(--stage);
    font-family: "Jost", sans-serif;
    color: var(--ink);
    position: relative;
  }
  .card {
    position: absolute;
    top: 172px;
    width: 520px;
    height: 288px;
    background: var(--ink);
    border-radius: 14px;
    overflow: hidden;
  }
  .card--front { left: 50px; }
  .card--back { left: 630px; }

  /* front */
  .rule {
    position: absolute;
    left: 16px;
    width: 254px;
    height: 2px;
    background: var(--paper);
  }
  .rule--top { top: 14px; }
  .rule--bottom { bottom: 14px; }
  .tagline {
    position: absolute;
    left: 26px;
    top: 112px;
    width: 240px;
    color: var(--paper);
    font-size: 21px;
    line-height: 1.3;
    font-weight: 400;
  }
  .brand-panel {
    position: absolute;
    background: var(--paper);
    display: flex;
    flex-direction: column;
    align-items: center;
    justify-content: center;
    gap: 14px;
  }
  .card--front .brand-panel { left: 282px; top: 14px; width: 224px; height: 260px; }
  .card--back .brand-panel { left: 14px; top: 14px; width: 232px; height: 260px; }
  .brand-mark {
    width: 128px;
    height: 128px;
    border: 2px solid var(--ink);
  }
  .brand-name {
    font-size: 17px;
    font-weight: 500;
    letter-spacing: 0.06em;
    text-transform: uppercase;
    text-align: center;
    line-height: 1.2;
    color: var(--ink);
  }

  /* back */
  .details {
    position: absolute;
    left: 282px;
    top: 14px;
    width: 224px;
    height: 260px;
    background: var(--paper);
    padding: 20px 18px 22px 10px;
    text-align: right;
    display: flex;
    flex-direction: column;
  }
  .person-name { font-size: 22px; font-weight: 600; line-height: 1.1; }
  .person-role { font-size: 15px; color: var(--muted); margin-top: 2px; }
  .contact { margin-top: auto; font-size: 15px; line-height: 1.6; }

  /* flip hint */
  .flip-arrow { position: absolute; left: 572px; top: 306px; }
</style>
</head>
<body>
  <section class="card card--front" aria-label="Card front">
    <div class="rule rule--top"></div>
    <div class="rule rule--bottom"></div>
    <p class="tagline">Designer style,<br>quietly priced</p>
    <div class="brand-panel">
      <div class="brand-mark"></div>
      <p class="brand-name">The Brightwell<br>Apparel House</p>
    </div>
  </section>

  <svg class="flip-arrow" width="56" height="20" viewBox="0 0 56 20" aria-hidden="true">
    <line x1="10" y1="10" x2="54" y2="10" stroke="#0b0b0b" stroke-width="2" stroke-dasharray="6 5"/>
    <polygon points="2,10 12,4 12,16" fill="#0b0b0b"/>
  </svg>

  <section class="card card--back" aria-label="Card back">
    <div class="brand-panel">
      <div class="brand-mark"></div>
      <p class="brand-name">The Brightwell<br>Apparel House</p>
    </div>
    <div class="details">
      <p class="person-name">Daniel Marsh</p>
      <p class="person-role">general manager</p>
      <p class="contact">
        t +1 212 555 0147<br>
        f +1 212 555 0192<br>
        marsh@brightwell.com
      </p>
    </div>
  </section>
</body>
</html>
```